The Fresh Body Hour with Dan Corbell.

I'm launching this podcast on health and wellness and I want to be take serious. That starts with a great design. There's too much contradiction out there about what is and isn't healthy. I want my podcast to be a resource that people can rely upon. I want my face in it and I want it to pop with colors that catch the eye. I want It clean and crisp. I was also thinking of experimenting with an animated photo of me as well. What ever looks best.

Industry/Entity Type

Health And Wellness

Font styles to use
Sans Serif

Requirements
Must have
• My face and or body.

```html
<!DOCTYPE html>
<html lang="en">
<head>
<meta charset="utf-8">
<title>The Fresh Body Hour with Dan Corbell – Podcast Cover</title>
<link href="https://fonts.googleapis.com/css2?family=Alfa+Slab+One&family=Archivo:ital,wght@1,600;1,900&display=swap" rel="stylesheet">
<style>
  :root {
    --page: #ffffff;
    --frame: #d23a2a;
    --bg-top: #f7a75c;
    --bg-mid: #f59a7a;
    --bg-bottom: #f6b3ae;
    --skin-light: #f2b27e;
    --skin-deep: #d9714a;
    --ink: #111111;
    --paper: #ffffff;
    --name-red: #b3141a;
    --shadow-warm: rgba(214, 86, 60, 0.55);
  }
  * { box-sizing: border-box; margin: 0; padding: 0; }
  html, body {
    width: 1200px; height: 754px; overflow: hidden;
    background: var(--page);
  }
  .stage { position: relative; width: 1200px; height: 754px; }

  .cover {
    --s: 1;
    position: absolute;
    width: calc(640px * var(--s));
    height: calc(640px * var(--s));
    border: 1px solid var(--frame);
    overflow: hidden;
    background:
      radial-gradient(ellipse at 85% 95%, rgba(255,220,220,0.8), transparent 55%),
      linear-gradient(180deg, var(--bg-top) 0%, var(--bg-mid) 55%, var(--bg-bottom) 100%);
  }
  .cover--large { left: 57px; top: 57px; }
  .cover--small { --s: 0.575; left: 760px; top: 192px; }

  .cover__portrait {
    position: absolute; left: 0; top: 0;
    width: 50%; height: 100%;
    background:
      radial-gradient(ellipse at 40% 40%, var(--skin-light) 0%, var(--skin-deep) 60%, transparent 85%),
      linear-gradient(90deg, rgba(217,113,74,0.7), rgba(245,154,122,0));
  }

  .cover__title {
    position: absolute;
    right: calc(22px * var(--s));
    top: calc(70px * var(--s));
    text-align: right;
    white-space: nowrap;
  }
  .cover__title span { display: block; }

  .title__lead, .title__main {
    font-family: "Alfa Slab One", serif;
    paint-order: stroke fill;
    text-shadow: calc(6px * var(--s)) calc(6px * var(--s)) 0 var(--shadow-warm);
  }
  .title__lead {
    font-size: calc(58px * var(--s));
    line-height: calc(72px * var(--s));
    color: var(--paper);
    -webkit-text-stroke: calc(5px * var(--s)) var(--ink);
  }
  .title__main {
    font-size: calc(66px * var(--s));
    line-height: calc(78px * var(--s));
    color: var(--ink);
    -webkit-text-stroke: calc(4px * var(--s)) var(--paper);
  }
  .title__format {
    font-family: "Archivo", sans-serif;
    font-style: italic; font-weight: 900;
    font-size: calc(72px * var(--s));
    line-height: calc(86px * var(--s));
    color: var(--paper);
    -webkit-text-stroke: calc(4px * var(--s)) var(--ink);
    paint-order: stroke fill;
    text-shadow: calc(6px * var(--s)) calc(6px * var(--s)) 0 var(--shadow-warm);
  }
  .title__with {
    font-family: "Archivo", sans-serif;
    font-style: italic; font-weight: 600;
    font-size: calc(46px * var(--s));
    line-height: calc(62px * var(--s));
    margin-top: calc(8px * var(--s));
    color: var(--paper);
    -webkit-text-stroke: calc(4px * var(--s)) var(--ink);
    paint-order: stroke fill;
  }
  .host {
    font-family: "Alfa Slab One", serif;
    color: var(--name-red);
    -webkit-text-stroke: calc(5px * var(--s)) var(--paper);
    paint-order: stroke fill;
    text-shadow: calc(7px * var(--s)) calc(7px * var(--s)) 0 var(--shadow-warm);
  }
  .host__first {
    font-size: calc(104px * var(--s));
    line-height: calc(100px * var(--s));
  }
  .host__last {
    font-size: calc(70px * var(--s));
    line-height: calc(92px * var(--s));
  }
</style>
</head>
<body>
<main class="stage">
  <section class="cover cover--large">
    <div class="cover__portrait" role="img" aria-label="Photo of host Dan Corbell, shirtless and athletic"></div>
    <h1 class="cover__title">
      <span class="title__lead">The Fresh</span>
      <span class="title__main">Body</span>
      <span class="title__format">HOUR</span>
      <span class="title__with">with</span>
      <span class="host host__first">DAN</span>
      <span class="host host__last">CORBELL</span>
    </h1>
  </section>

  <section class="cover cover--small">
    <div class="cover__portrait" role="img" aria-label="Photo of host Dan Corbell, shirtless and athletic"></div>
    <h2 class="cover__title">
      <span class="title__lead">The Fresh</span>
      <span class="title__main">Body</span>
      <span class="title__format">HOUR</span>
      <span class="title__with">with</span>
      <span class="host host__first">DAN</span>
      <span class="host host__last">CORBELL</span>
    </h2>
  </section>
</main>
</body>
</html>
```